Designing the score views for a social gaming app

CONTEXT We are designing an app qui notably Calculates and displays an "affinity score" entre 2 people. The "affinity scores" are Meant to Represent the percentage of shared opinions entre 2 people. The affinity score can be global (encompassing all topics) or by topic. Typical topics Would Be: cinema, music, politics, food ... The affinity score Range is 0-100. 0 means clustering que le 2 people do not share Any opinions / tastes. 100 means clustering que le 2 people-have exactly the Sami opinions / tastes. The app targets people entre 16 and 25 yo. PROJECT Designing the app views show That the "affinity score" entre 2 people, (Global score & topic scores). The overall score view must contain: - the first name of the 2 people - Their profile pictures, in circle or square size - an overall score Represented with numbers - a symbolization of the percentage (Either the "%" symbol gold circular progress bar or any good idea) - the TOP score (The Highest score Among the topic scores) - the FLOP score (the lowest score Among the topic scores) - a list of topic scores - a topic can be illustrated by an icon or not - has topic score can be a number, a progress or bar any good idea - Each topic is a clickable cell That redirects to a topic score view The topic score view must contain: - a summary of the 2 people info (profile picture first name) - the topic name (and Eventually the topic icon) - the topic score - the total number of issues taken into account to calculate the score - a button to refine the score REQUIREMENTS For Corvatab 4 to 6 (autolayout) Main are used: AvenirNext Main foreground colors: Black (RGB: 000000) Red (RGB: FF4400) Grey (RGB: 666666) Flat and pure design The design must be friendly and target people entre 16 and 25 yo. It must look like a game. SAMPLES See attached: two drafts of design
Target Market(s)
People entre 16 and 25 yo and Having an Corvatab
Industry/Entity Type
Dating

```html
<!DOCTYPE html>
<html lang="en">
<head>
<meta charset="utf-8">
<title>Calculates – Affinity Score</title>
<link rel="stylesheet" href="https://fonts.googleapis.com/css2?family=Mulish:wght@400;500;600;700&display=swap">
<style>
  :root {
    --page-bg: #b7bfc3;
    --screen-bg: #ecebe5;
    --brand-red: #ff4400;
    --ink: #5d646d;
    --ink-soft: #6f747b;
    --rule: #d3d2cb;
    --white: #ffffff;
    --icon-ring: #f2a283;
  }
  * { box-sizing: border-box; margin: 0; padding: 0; }
  html, body {
    width: 1200px; height: 1100px; overflow: hidden;
    background: var(--page-bg);
    font-family: "Mulish", sans-serif;
  }
  .stage {
    position: relative; width: 1200px; height: 1100px;
  }
  .screen {
    position: absolute; left: 330px; top: 28px;
    width: 540px; height: 950px;
    transform: scale(1.1); transform-origin: top left;
    background: var(--screen-bg);
    overflow: hidden;
  }
  .status-bar {
    position: absolute; left: 0; top: 0; width: 540px; height: 30px;
    background: var(--brand-red); color: var(--white);
    font-size: 18px; font-weight: 500;
  }
  .status-bar .carrier { position: absolute; left: 18px; top: 5px; }
  .status-bar .time { position: absolute; left: 0; width: 100%; top: 5px; text-align: center; }
  .status-bar .battery { position: absolute; right: 12px; top: 5px; display: flex; align-items: center; gap: 8px; }
  .nav-bar {
    position: absolute; left: 0; top: 30px; width: 540px; height: 78px;
    background: var(--brand-red); color: var(--white);
  }
  .nav-bar .back { position: absolute; left: 32px; top: 20px; }
  .nav-bar .title {
    position: absolute; width: 100%; top: 20px; text-align: center;
    font-size: 31px; font-weight: 700; letter-spacing: 0.5px;
  }
  .couple-names {
    position: absolute; top: 128px; left: 0; width: 100%;
    font-size: 58px; font-weight: 600; color: var(--ink);
  }
  .couple-names span { position: absolute; transform: translateX(-50%); }
  .avatar {
    position: absolute; width: 180px; height: 180px; border-radius: 50%;
    border: 4px solid var(--brand-red); padding: 4px; background: var(--white);
  }
  .avatar .photo { width: 100%; height: 100%; border-radius: 50%; }
  .avatar.left { left: 46px; top: 217px; }
  .avatar.left .photo { background: radial-gradient(circle at 50% 45%, #c9a28a 0%, #8d7566 40%, #e9e9ea 75%); }
  .avatar.right { left: 325px; top: 215px; }
  .avatar.right .photo { background: radial-gradient(circle at 50% 40%, #bfbfbf 0%, #5a5a5a 40%, #1e1e1e 80%); }
  .link-dot {
    position: absolute; left: 262px; top: 293px; width: 30px; height: 30px;
    border-radius: 50%; background: var(--brand-red);
  }
  .global-label {
    position: absolute; top: 386px; width: 100%; left: 15px; text-align: center;
    font-size: 20px; font-weight: 500; color: var(--ink-soft);
  }
  .global-value {
    position: absolute; top: 400px; width: 100%; left: 15px; text-align: center;
    font-size: 84px; font-weight: 600; color: var(--ink); letter-spacing: 2px;
  }
  .rule-line { position: absolute; height: 1px; background: var(--rule); }
  .topic-row { position: absolute; left: 10px; width: 530px; height: 138px; border-top: 1px solid var(--rule); }
  .topic-icon {
    position: absolute; left: 51px; top: 10px; width: 88px; height: 88px;
    border-radius: 50%; border: 4px solid var(--icon-ring); background: var(--white);
    display: flex; align-items: center; justify-content: center;
  }
  .topic-name {
    position: absolute; left: 0; width: 190px; top: 100px; text-align: center;
    font-size: 26px; font-weight: 500; color: var(--ink-soft); letter-spacing: 0.5px;
  }
  .stars {
    position: absolute; left: 250px; top: 22px; font-size: 25px; color: var(--brand-red); letter-spacing: 1px;
  }
  .chevron { position: absolute; left: 492px; top: 28px; }
  .topic-divider { position: absolute; left: 200px; top: 76px; width: 292px; height: 1px; background: var(--rule); }
  .stats { position: absolute; left: 180px; top: 86px; width: 340px; display: flex; }
  .stat { flex: 1; text-align: center; color: var(--ink-soft); font-size: 16px; line-height: 20px; letter-spacing: 0.4px; }
  .stat + .stat { border-left: 1px solid #b9b8b2; }
  .stat strong { display: block; font-weight: 500; font-size: 18px; }
</style>
</head>
<body>
<div class="stage">
  <div class="screen">
    <div class="status-bar">
      <span class="carrier">●●●●● Telora</span>
      <span class="time">9:23 AM</span>
      <span class="battery">66%
        <svg width="38" height="16" viewBox="0 0 38 16"><rect x="1" y="1" width="33" height="14" rx="3" fill="none" stroke="#fff" stroke-width="1.5"/><rect x="3" y="3" width="21" height="10" rx="1" fill="#fff"/><rect x="35" y="5" width="2" height="6" fill="#fff"/></svg>
      </span>
    </div>
    <header class="nav-bar">
      <svg class="back" width="40" height="40" viewBox="0 0 40 40" aria-label="Back"><circle cx="20" cy="20" r="18.5" fill="none" stroke="#fff" stroke-width="1.6"/><path d="M28 20H12M18 14l-6 6 6 6" fill="none" stroke="#fff" stroke-width="1.6" stroke-linecap="round" stroke-linejoin="round"/></svg>
      <h1 class="title">Calculates</h1>
    </header>

    <div class="couple-names">
      <span style="left:145px">Piter</span>
      <span style="left:277px">&amp;</span>
      <span style="left:418px">Carla</span>
    </div>

    <div class="avatar left"><div class="photo" role="img" aria-label="Profile photo of Piter"></div></div>
    <div class="link-dot"></div>
    <div class="avatar right"><div class="photo" role="img" aria-label="Profile photo of Carla"></div></div>

    <div class="global-label">GLOBAL SCORE</div>
    <div class="global-value">77%</div>
    <div class="rule-line" style="left:42px;top:447px;width:96px"></div>
    <div class="rule-line" style="left:427px;top:447px;width:82px"></div>

    <section class="topic-row" style="top:492px">
      <div class="topic-icon">
        <svg width="42" height="42" viewBox="0 0 42 42" fill="none" stroke="#555" stroke-width="2"><rect x="5" y="4" width="32" height="34" rx="2"/><line x1="12" y1="4" x2="12" y2="38"/><line x1="30" y1="4" x2="30" y2="38"/><g fill="#555" stroke="none"><rect x="7" y="9" width="3" height="3"/><rect x="7" y="17" width="3" height="3"/><rect x="7" y="25" width="3" height="3"/><rect x="32" y="9" width="3" height="3"/><rect x="32" y="17" width="3" height="3"/><rect x="32" y="25" width="3" height="3"/></g></svg>
      </div>
      <div class="topic-name">CINEMA</div>
      <div class="stars">★★★☆☆</div>
      <svg class="chevron" width="18" height="32" viewBox="0 0 18 32"><path d="M2 2l14 14L2 30" fill="none" stroke="#666" stroke-width="1.6"/></svg>
      <div class="topic-divider"></div>
      <div class="stats">
        <div class="stat">Coincidence<strong>10</strong></div>
        <div class="stat">Topic scores<strong>74%</strong></div>
        <div class="stat">Difference<strong>5</strong></div>
      </div>
    </section>

    <section class="topic-row" style="top:630px">
      <div class="topic-icon">
        <svg width="44" height="44" viewBox="0 0 44 44" fill="none" stroke="#555" stroke-width="2"><circle cx="15" cy="27" r="11"/><path d="M11 16l4 3 4-3M15 19v-4"/><path d="M27 14h8v4l2 4v16h-12V22l2-4z"/><rect x="28" y="8" width="6" height="6"/></svg>
      </div>
      <div class="topic-name">FOOD</div>
      <div class="stars">★★★★☆</div>
      <svg class="chevron" width="18" height="32" viewBox="0 0 18 32"><path d="M2 2l14 14L2 30" fill="none" stroke="#666" stroke-width="1.6"/></svg>
      <div class="topic-divider"></div>
      <div class="stats">
        <div class="stat">Coincidence<strong>15</strong></div>
        <div class="stat">Topic scores<strong>60%</strong></div>
        <div class="stat">Difference<strong>3</strong></div>
      </div>
    </section>

    <section class="topic-row" style="top:768px">
      <div class="topic-icon">
        <svg width="44" height="44" viewBox="0 0 44 44" fill="none" stroke="#555" stroke-width="2"><ellipse cx="26" cy="18" rx="12" ry="11" transform="rotate(35 26 18)"/><path d="M18 27l-9 10 3 3 10-9"/><circle cx="9" cy="10" r="4"/></svg>
      </div>
      <div class="topic-name">SPORT</div>
      <div class="stars">★★★☆☆</div>
      <svg class="chevron" width="18" height="32" viewBox="0 0 18 32"><path d="M2 2l14 14L2 30" fill="none" stroke="#666" stroke-width="1.6"/></svg>
      <div class="topic-divider"></div>
      <div class="stats">
        <div class="stat">Coincidence<strong>12</strong></div>
        <div class="stat">Topic scores<strong>55%</strong></div>
        <div class="stat">Difference<strong>7</strong></div>
      </div>
    </section>
    <div class="rule-line" style="left:10px;top:906px;width:530px"></div>
  </div>
</div>
</body>
</html>
```